Healthcare Recruitment Agency Brochure

We need our current Brochure updated as its old and dated. The brochure will be for our current and potential Clients and should provide all the necessary information regarding our services, but in a well presented, easy reading format which echoes our company Brand. The company supplies Healthcare establishments with trained healthcare Staff which can be in a variety of settings.
UPDATE: Following the submission of many designs we would like to amend the information/content to be included in the brochure and have uploaded additional information. We would like an 8 page booklet with the various sections spread out so as not to look to 'wordy' page 1 Front cover, 2 About Us, 3 Our Service, 4 Our promise, 5 Our Staff, 6 Our Ethos, 7 What Our Clients Say/Testimonials, 8 Contact Us/Back page. Please if using pictures (which is welcomed) steer away from the surgical/doctor type. We mainly provide care to the Elderly within Nursing and Residential Homes and Support Environments. Thanks
Updates

Target Market(s)

Healthcare clientell

Industry/Entity Type

Healthcare

Requirements
Must have
• Pictures, animation, easy reading, informative, tie in with website theme www.carewellstaffline.example
Nice to have
• open to ideas
Should not have
• very long text paragraphs

```html
<!DOCTYPE html>
<html lang="en">
<head>
<meta charset="utf-8">
<title>Carewell Staffline Brochure</title>
<link rel="stylesheet" href="https://fonts.googleapis.com/css2?family=Poppins:wght@400;500;600;800&family=Open+Sans:ital,wght@0,400;0,600;1,400&display=swap">
<style>
:root{
  --teal:#1f9e8c;
  --teal-dark:#14826f;
  --teal-soft:#7cc3bd;
  --blue:#1f4fae;
  --blue-deep:#1b3a8a;
  --ink:#2b3550;
  --paper:#ffffff;
  --paper-shade:#eef1f7;
  --stage:#2a2a2b;
}
*{box-sizing:border-box;margin:0;padding:0}
html,body{width:920px;height:1200px;overflow:hidden}
body{background:var(--stage);font-family:"Open Sans",sans-serif;color:var(--ink);position:relative}
.spread{position:absolute;left:70px;width:780px;height:540px;display:flex;box-shadow:0 18px 40px rgba(0,0,0,.55)}
.spread--covers{top:40px}
.spread--inside{top:620px}
.page{position:relative;width:390px;height:540px;background:var(--paper);overflow:hidden}
.page + .page{border-left:1px solid #d8dde8}
.page svg.art{position:absolute;inset:0;width:390px;height:540px}

/* Ethos page */
.ethos{position:absolute;left:30px;right:30px;top:256px;text-align:center}
.ethos__title{font-family:"Poppins",sans-serif;font-weight:500;font-size:17px;color:var(--ink);line-height:1.25}
.ethos__rule{width:190px;height:3px;background:var(--teal);margin:5px auto 10px}
.value{margin-bottom:8px}
.value__name{font-family:"Poppins",sans-serif;font-weight:600;font-size:13px;line-height:1.4;color:var(--blue)}
.value__text{font-size:7.5px;line-height:1.45;color:var(--blue-deep)}

/* Front cover */
.brand{position:absolute;left:0;right:0;top:330px;text-align:center;font-family:"Poppins",sans-serif;font-weight:500;font-size:34px;color:var(--blue);letter-spacing:.5px}
.brand__dot{display:inline-block;width:14px;height:14px;border-radius:50%;background:var(--teal);margin-right:10px;vertical-align:middle}
.cover__url{position:absolute;left:0;right:0;bottom:0;height:42px;background:var(--blue);color:#fff;font-size:11px;text-align:right;padding:14px 28px 0 0}

/* Inside pages */
.heading{font-family:"Poppins",sans-serif;font-weight:800;font-size:17px;color:#1c1f2a}
.heading__rule{width:90px;height:3px;background:var(--blue);margin:2px 0 8px}
.body-text{font-size:7px;line-height:1.5;margin-bottom:6px}
.about{position:absolute;left:24px;top:28px;width:230px}
.callout{background:var(--blue);color:#fff;font-size:7px;line-height:1.5;padding:6px 8px;margin:6px 0 8px;font-style:italic}
.checklist{list-style:none}
.checklist li{position:relative;padding-left:16px;font-size:7px;line-height:1.45;margin-bottom:6px;color:var(--blue-deep);font-style:italic}
.checklist li::before{content:"";position:absolute;left:0;top:1px;width:9px;height:9px;border:1px solid var(--teal);border-radius:50%}
.checklist li::after{content:"";position:absolute;left:3px;top:3px;width:3px;height:5px;border:solid var(--teal);border-width:0 1px 1px 0;transform:rotate(45deg)}
.about__band{position:absolute;left:0;bottom:0;width:262px;height:16px;background:var(--blue)}
.about__photo{position:absolute;right:0;top:0;width:128px;height:540px;background:linear-gradient(160deg,#2aa596,#127a6c 60%,#0f6a5e)}

.staff{position:absolute;left:24px;top:28px;width:345px}
.staff .checklist{width:215px}
.staff .checklist li{font-style:normal;color:var(--ink);margin-bottom:5px}
.staff__photo{position:absolute;right:20px;top:150px;width:130px;height:175px;background:linear-gradient(180deg,#c9a88f,#e9e2dc 55%,#f4f4f6)}
.staff__closing{position:absolute;left:24px;top:380px;width:320px}
</style>
</head>
<body>

<section class="spread spread--covers">
  <!-- Back cover: Our Ethos -->
  <article class="page page--ethos">
    <svg class="art" viewBox="0 0 390 540">
      <defs>
        <linearGradient id="teamTone" x1="0" y1="0" x2="1" y2="1">
          <stop offset="0" stop-color="#a9d6d4"/><stop offset="1" stop-color="#6fb8b3"/>
        </linearGradient>
      </defs>
      <path d="M0 160 Q220 230 390 90 V150 Q230 255 0 250 Z" fill="var(--teal)"/>
      <path d="M0 0 H390 V90 Q220 220 0 180 Z" fill="url(#teamTone)" role="img" aria-label="Photo of a care team joining hands in celebration"/>
      <path d="M0 180 Q220 220 390 90" fill="none" stroke="#fff" stroke-width="3"/>
    </svg>
    <div class="ethos">
      <h2 class="ethos__title">Our Ethos<br>Carewell Staffline Ltd</h2>
      <div class="ethos__rule"></div>
      <div class="value"><h3 class="value__name">Honesty and Integrity.</h3><p class="value__text">We pride ourselves on being direct and straightforward in all our communication with our clients and potential candidates.</p></div>
      <div class="value"><h3 class="value__name">Dedication.</h3><p class="value__text">Our consultants aim to fully understand the requirements of our clients and candidates in order to find mutually beneficial solutions.</p></div>
      <div class="value"><h3 class="value__name">Service Excellence.</h3><p class="value__text">We aim to always deliver superior services to help both employers and candidates achieve their goals.</p></div>
      <div class="value"><h3 class="value__name">Leadership.</h3><p class="value__text">Our purpose is to become leaders in the healthcare recruitment sector, raising the bar for the entire industry.</p></div>
    </div>
  </article>

  <!-- Front cover -->
  <article class="page page--cover">
    <svg class="art" viewBox="0 0 390 540">
      <defs>
        <linearGradient id="gardenTone" x1="0" y1="0" x2="1" y2="1">
          <stop offset="0" stop-color="#8fb67a"/><stop offset="1" stop-color="#4e7f45"/>
        </linearGradient>
        <linearGradient id="visitTone" x1="0" y1="0" x2="1" y2="0">
          <stop offset="0" stop-color="#7aa7d6"/><stop offset="1" stop-color="#d9e3ef"/>
        </linearGradient>
      </defs>
      <path d="M0 215 Q200 280 390 190 V250 Q200 320 0 275 Z" fill="var(--teal)"/>
      <path d="M0 0 H390 V190 Q200 270 0 225 Z" fill="url(#gardenTone)" role="img" aria-label="Photo of a carer with an elderly resident in a garden"/>
      <path d="M150 250 Q250 130 390 120 V195 Q280 250 150 250 Z" fill="url(#visitTone)" role="img" aria-label="Photo of a clinician greeting an elderly patient"/>
      <path d="M150 250 Q250 130 390 120" fill="none" stroke="var(--blue)" stroke-width="5"/>
    </svg>
    <div class="brand"><span class="brand__dot"></span>Carewell Staffline</div>
    <div class="cover__url">www.carewellstaffline.example</div>
  </article>
</section>

<section class="spread spread--inside">
  <!-- About Us -->
  <article class="page page--about">
    <div class="about__photo" role="img" aria-label="Photo of a nurse holding a stethoscope, teal tinted"></div>
    <div class="about">
      <h2 class="heading">About Us</h2>
      <div class="heading__rule"></div>
      <p class="body-text">With over 15 years of experience Carewell Staffline specialises in reliable recruitment solutions for the healthcare sector.</p>
      <p class="body-text">We are StaffCare Board accredited so you can rest assured that we will always be working in line with current legislation and guidelines.</p>
      <p class="body-text">We strive for excellence in every aspect of our service, this includes ensuring that we are always fair, honest and supportive of our temporary staff members, which is why we are a National Living Wage Employer.</p>
      <div class="callout">We know that our Clients often have a lot on their plate, which is why we pride ourselves on being extremely accommodating:</div>
      <ul class="checklist">
        <li>We can visit you at a time to suit you, to discuss your requirements and our service.</li>
        <li>We will give you our client application pack including everything you need to know, to start booking staff from Carewell Staffline we simply need a completed client account form.</li>
        <li>We have staff available to work at the drop of a hat, we understand the need for urgency and will make it our mission to try to help you every time.</li>
        <li>Our friendly office staff will always be at the end of the phone to deal with your requests; we never outsource to call centres.</li>
        <li>We will never leave you waiting and always be honest and realistic in telling you whether we can help.</li>
        <li>When you have booked a staff member you will always receive their compliance form, in a format that suits you.</li>
        <li>You can choose how frequently and in which format we send you your staff rotas, we will be completely flexible to your needs.</li>
        <li>We are always interested in how we could improve; we will regularly review our service and come and visit you when requested.</li>
      </ul>
    </div>
    <div class="about__band"></div>
  </article>

  <!-- Our Staff -->
  <article class="page page--staff">
    <svg class="art" viewBox="0 0 390 540">
      <defs>
        <linearGradient id="waveTone" x1="0" y1="0" x2="1" y2="0">
          <stop offset="0" stop-color="#e3e6f5"/><stop offset="1" stop-color="#b9c4ee"/>
        </linearGradient>
      </defs>
      <path d="M0 470 Q150 450 260 480 T390 470 V540 H0 Z" fill="url(#waveTone)"/>
      <path d="M0 500 Q180 480 300 510 T390 500 V540 H0 Z" fill="#6f86d8" opacity=".55"/>
      <path d="M120 520 Q260 505 390 515 V540 H120 Z" fill="var(--blue)"/>
      <polyline points="20,480 60,480 66,466 72,494 78,480 200,480 206,470 212,490 218,480 300,480 306,462 312,498 318,480 370,480" fill="none" stroke="#9fb0ea" stroke-width="1"/>
    </svg>
    <div class="staff">
      <h2 class="heading">Our Staff</h2>
      <div class="heading__rule" style="background:var(--teal)"></div>
      <p class="body-text">All our candidates go through a thorough vetting and recruitment process and only ever commence assignments after the following:</p>
      <ul class="checklist">
        <li>A face-to-face interview and skills assessment has been undertaken</li>
        <li>Full employment history has been submitted</li>
        <li>Right to work has been recorded and verified</li>
        <li>Fitness to work has been declared</li>
        <li>Two work related references have been obtained and verified</li>
        <li>An enhanced DBS certificate has been provided</li>
        <li>In date, sufficient training certificates have been provided and verified or in house training courses have been attended and certificates issued</li>
        <li>Registration with the appropriate bodies has been verified for Registered Nurses</li>
        <li>A shadow shift has been completed if it is a brand new staff member</li>
        <li>An ID badge, uniform and timesheets have been issued</li>
      </ul>
    </div>
    <div class="staff__photo" role="img" aria-label="Photo of a smiling carer in a white uniform"></div>
    <div class="staff__closing">
      <p class="body-text">We understand that it is imperative for our clients to only have extremely competent, fully trained staff supporting their existing team. We are proud to cover the standards set within the Care Certificate in the training modules that we deliver to our staff.</p>
      <p class="body-text">All training is refreshed on an annual basis and we ensure that up to date certificates are held by all staff at all times.</p>
    </div>
  </article>
</section>

</body>
</html>
```